Men's and Boys sports themed barbershop. I was wanting to see what a black card would look like. I think white is too plain, but I am just needing some ideas for a design or background.

Contact Information for Business Card

ACE Trims
4586 E. Harbor Pine Rd
Crystal River, Fl 36917
(352) 555-0143
ace_trims@fernmail.com
Denise Marlow (on one side) Greg Marlow (on opposite side)
Owner
(352) 555-0178 (Denise) (352) 555-0192

```html
<!DOCTYPE html>
<html lang="en">
<head>
<meta charset="utf-8">
<title>ACE Trims – Business Card</title>
<link rel="stylesheet" href="https://fonts.googleapis.com/css2?family=Questrial&family=Montserrat:wght@600&display=swap">
<style>
  :root {
    --page: #d9d9d9;
    --card: #26282c;
    --text: #d2d3d6;
    --muted: #a9abb0;
    --accent: #d7202d;
    --brand: #e7e8ea;
  }
  * { margin: 0; padding: 0; box-sizing: border-box; }
  html, body { width: 1200px; height: 900px; overflow: hidden; }
  body {
    background: var(--page);
    font-family: "Questrial", "Century Gothic", sans-serif;
    position: relative;
  }
  .card {
    position: absolute;
    left: 75px; top: 150px;
    width: 1050px; height: 600px;
    background: var(--card);
    color: var(--text);
    box-shadow: 0 8px 24px rgba(0,0,0,.25);
  }
  .brand {
    position: absolute;
    right: 80px; top: 70px;
    display: flex; align-items: center; gap: 16px;
  }
  .brand-dot {
    width: 22px; height: 22px; border-radius: 50%;
    background: var(--accent);
  }
  .brand-name {
    font-size: 62px; color: var(--brand); letter-spacing: 1px; line-height: 1;
  }
  .owner {
    position: absolute; left: 90px; top: 300px;
  }
  .owner-name {
    font-family: "Montserrat", "Century Gothic", sans-serif;
    font-weight: 600; font-size: 27px; letter-spacing: 1.5px; color: var(--text);
  }
  .owner-role { font-size: 21px; color: var(--muted); margin-top: 4px; }
  .address {
    position: absolute; left: 90px; top: 430px;
    font-size: 23px; line-height: 1.45; color: var(--muted);
  }
  .contacts { position: absolute; list-style: none; }
  .contacts li {
    display: flex; align-items: center; gap: 12px;
    font-size: 21px; line-height: 1; color: var(--muted); margin-bottom: 10px;
  }
  .contacts svg { width: 22px; height: 22px; flex: none; }
  .phones { left: 520px; top: 390px; }
  .web { left: 770px; top: 315px; }
</style>
</head>
<body>
  <section class="card" aria-label="ACE Trims business card">
    <div class="brand">
      <span class="brand-dot"></span>
      <span class="brand-name">ACE Trims</span>
    </div>

    <div class="owner">
      <p class="owner-name">GREG MARLOW</p>
      <p class="owner-role">Owner</p>
    </div>

    <p class="address">4586 E. Harbor Pine Rd<br>Crystal River, Fl 36917</p>

    <ul class="contacts phones">
      <li>
        <svg viewBox="0 0 24 24" aria-hidden="true"><circle cx="12" cy="12" r="12" fill="var(--accent)"/><path d="M8.2 6.5l2 2.3-1.1 1.5c.8 1.7 2 2.9 3.6 3.6l1.5-1.1 2.3 2-1.3 1.7c-4 -.3-7.2-3.5-7.5-7.5z" fill="var(--card)"/></svg>
        <span>(352) 555-0178</span>
      </li>
      <li>
        <svg viewBox="0 0 24 24" aria-hidden="true"><rect width="24" height="24" rx="5" fill="var(--accent)"/><rect x="8" y="5" width="8" height="14" rx="1.5" fill="none" stroke="var(--card)" stroke-width="1.6"/><circle cx="12" cy="16.5" r="1" fill="var(--card)"/></svg>
        <span>(352) 555-0143</span>
      </li>
    </ul>

    <ul class="contacts web">
      <li>
        <svg viewBox="0 0 24 24" aria-hidden="true"><circle cx="12" cy="12" r="12" fill="var(--accent)"/><rect x="6" y="8" width="12" height="8" rx="1" fill="none" stroke="var(--card)" stroke-width="1.5"/><path d="M6.5 8.5l5.5 4 5.5-4" fill="none" stroke="var(--card)" stroke-width="1.5"/></svg>
        <span>info@acetrimsfern.com</span>
      </li>
      <li>
        <svg viewBox="0 0 24 24" aria-hidden="true"><circle cx="12" cy="12" r="12" fill="var(--accent)"/><circle cx="12" cy="12" r="6.5" fill="none" stroke="var(--card)" stroke-width="1.4"/><ellipse cx="12" cy="12" rx="2.8" ry="6.5" fill="none" stroke="var(--card)" stroke-width="1.2"/><path d="M5.5 12h13" stroke="var(--card)" stroke-width="1.2"/></svg>
        <span>www.acetrimsfern.com</span>
      </li>
    </ul>
  </section>
</body>
</html>
```